Website redesign for a technology and engineering company

We'd like to redesign our website which can be found on quorvane.co.nz
!! Please find the designers brief as an uploaded file with all details in there!!
The main purpose for redesign is:
>change of services offered
>old website not very user friendly to maintain or update
Key requirements:
>visually appealing
>easy to navigate
>simple and easy to read
>responsive
>mobile device compatibility
>integrating best SEO practice
All the details are in the attached designer brief document.

```html
<!DOCTYPE html>
<html lang="en">
<head>
<meta charset="utf-8">
<title>Quorvane — Precision. Efficiency. Clarity.</title>
<link href="https://fonts.googleapis.com/css2?family=Roboto:wght@300;400;500;700&display=swap" rel="stylesheet">
<style>
:root{
  --blue:#3b6ef0;
  --blue-dark:#2f5fe0;
  --ink:#1d1d1f;
  --text:#444;
  --muted:#777;
  --light:#efefef;
  --white:#fff;
  --footer:#2b2b2b;
  --footer-line:#444;
}
*{margin:0;padding:0;box-sizing:border-box}
html,body{width:1200px;height:3592px;overflow:hidden}
body{font-family:"Roboto",Arial,sans-serif;color:var(--ink);background:var(--white);position:relative}
.abs{position:absolute}
a{color:inherit;text-decoration:none}

/* header */
.site-header{position:absolute;left:0;top:0;width:1200px;height:91px;border-bottom:1px solid #e6e6e6;background:var(--white)}
.brand{position:absolute;left:109px;top:26px;display:flex;align-items:center;gap:10px;font-size:32px;font-weight:500;color:var(--ink)}
.brand-dot{width:14px;height:14px;border-radius:50%;background:var(--ink)}
.main-nav{position:absolute;top:36px;left:0;font-size:14px;color:#555}
.main-nav a{position:absolute;white-space:nowrap}
.main-nav .active{font-weight:500;color:var(--ink)}
.call{position:absolute;left:756px;top:27px;display:flex;align-items:center;gap:10px}
.call-icon{width:34px;height:34px;border-radius:50%;box-shadow:0 2px 8px rgba(0,0,0,.15);display:flex;align-items:center;justify-content:center}
.call-label{font-size:13px;color:var(--blue);line-height:16px}
.call-number{font-size:15px;color:var(--ink);line-height:18px}
.btn{display:inline-flex;align-items:center;justify-content:center;background:var(--blue);color:var(--white);font-weight:500;font-size:15px;border-radius:20px;box-shadow:0 4px 8px rgba(59,110,240,.3)}
.header-cta{position:absolute;left:965px;top:25px;width:124px;height:38px}

/* hero */
.hero{position:absolute;left:0;top:91px;width:1200px;height:610px;overflow:hidden}
.hero-watermark{position:absolute;left:-20px;top:30px;font-size:120px;font-weight:700;color:#ececec;letter-spacing:2px}
.hero-title{position:absolute;left:209px;top:160px;font-size:62px;font-weight:700;line-height:77px;color:#222}
.hero-cta{position:absolute;left:212px;top:415px;width:124px;height:36px}
.hero-photo{position:absolute;left:609px;top:69px;width:432px;height:432px;border-radius:50%;background:radial-gradient(circle at 50% 25%,#cfd3d6 0,#b9bfc4 30%,#6f9a3e 55%,#4d7a2a 100%);box-shadow:0 0 0 8px #e4e4e4}

/* section headings */
.section-title{position:absolute;left:0;width:1200px;text-align:center;font-size:44px;font-weight:500;color:#222}

/* services */
.services{position:absolute;left:0;top:701px;width:1200px;height:514px;background:var(--light)}
.service-card{position:absolute;top:181px;width:310px;height:261px;background:var(--white);border-radius:6px;box-shadow:0 2px 10px rgba(0,0,0,.05);padding:0 21px}
.service-icon{position:absolute;left:23px;top:30px;width:70px;height:70px;border-radius:50%;background:#e9eefb;display:flex;align-items:center;justify-content:center}
.service-card h3{position:absolute;left:21px;top:120px;font-size:22px;font-weight:400;color:#222}
.service-card ul{position:absolute;left:21px;top:154px;list-style:none;font-size:12.5px;color:#333;line-height:20px}
.service-card li::before{content:"›";color:var(--blue);margin-right:6px}
.learn{font-size:14px;font-weight:500;color:var(--blue)}
.service-card .learn{position:absolute;left:21px;top:224px}

/* case studies */
.cases{position:absolute;left:0;top:1215px;width:1200px;height:837px;background:var(--blue)}
.cases-panel{position:absolute;left:65px;top:0;width:1135px;height:837px;background:var(--white);border-bottom-left-radius:240px;overflow:hidden}
.cases-photo{position:absolute;left:0;top:480px;width:1135px;height:357px;background:linear-gradient(180deg,#eef0f2 0,#9aa6ae 35%,#6e7a6a 65%,#7a6a46 100%)}
.case-card{position:absolute;width:436px;height:184px;background:var(--white);border-radius:0 0 30px 0;box-shadow:0 4px 16px rgba(0,0,0,.08)}
.case-card.featured{background:var(--blue);color:var(--white)}
.case-thumb{position:absolute;left:19px;top:25px;width:125px;height:136px;border-radius:4px;background:linear-gradient(180deg,#6f94c4 0,#9bb2c9 45%,#7a7a74 70%,#55524c 100%)}
.case-body{position:absolute;left:173px;top:22px;width:245px}
.case-body h3{font-size:16.5px;font-weight:500;line-height:26px;color:#222}
.case-body p{font-size:12px;font-weight:300;line-height:19px;color:#666;margin-top:6px;height:57px;overflow:hidden}
.case-body .learn{display:block;margin-top:6px}
.featured .case-body h3,.featured .case-body p,.featured .learn{color:var(--white)}

/* about */
.about{position:absolute;left:0;top:2052px;width:1200px;height:534px;background:var(--blue);color:var(--white)}
.about h2{position:absolute;left:111px;top:116px;font-size:44px;font-weight:500}
.about p{position:absolute;left:111px;top:185px;width:405px;font-size:15.3px;line-height:25.7px}
.about-cta{position:absolute;left:111px;top:417px;width:124px;height:36px;background:var(--white);color:var(--ink);box-shadow:0 4px 8px rgba(0,0,0,.15)}
.about-photo{position:absolute;left:553px;top:143px;width:532px;height:254px;border-radius:127px;background:linear-gradient(90deg,#6b6a58 0,#8b8a74 30%,#4a6a3a 60%,#6a7a48 100%)}

/* contact */
.contact{position:absolute;left:0;top:2586px;width:1200px;height:645px}
.field{position:absolute;width:383px;height:63px;background:var(--white);box-shadow:0 3px 14px rgba(0,0,0,.09);border-radius:3px;padding:22px 22px;font-size:13px;color:#666}
.field.message{width:791px;height:121px}
.submit{position:absolute;left:538px;top:531px;width:124px;height:36px}

/* footer */
.site-footer{position:absolute;left:0;top:3231px;width:1200px;height:361px;background:var(--footer);color:#e6e6e6}
.footer-brand{position:absolute;left:109px;top:120px;display:flex;align-items:center;gap:14px;font-size:46px;font-weight:500;color:var(--white)}
.footer-brand .brand-dot{width:20px;height:20px;background:var(--white)}
.footer-divider{position:absolute;left:391px;top:66px;width:1px;height:170px;background:var(--footer-line)}
.footer-col{position:absolute;top:70px}
.footer-col h4{font-size:20px;font-weight:500;color:var(--white);margin-bottom:12px}
.footer-col ul{list-style:none;font-size:15px;line-height:25.5px}
.footer-col li::before{content:"»";margin-right:12px}
.contact-line{display:flex;gap:10px;font-size:15px;line-height:25px;margin-bottom:16px}
.contact-line svg{flex:none;margin-top:5px}
.footer-bottom{position:absolute;left:109px;top:272px;width:982px;height:1px;background:var(--footer-line)}
.copyright{position:absolute;left:0;top:306px;width:1200px;text-align:center;font-size:15px}
</style>
</head>
<body>

<header class="site-header">
  <a class="brand" href="#"><span class="brand-dot"></span>Quorvane</a>
  <nav class="main-nav">
    <a class="active" style="left:358px" href="#">Home</a>
    <a style="left:429px" href="#">Services</a>
    <a style="left:517px" href="#">Projects</a>
    <a style="left:602px" href="#">About</a>
    <a style="left:673px" href="#">Contact</a>
  </nav>
  <div class="call">
    <span class="call-icon"><svg width="14" height="14" viewBox="0 0 24 24"><path fill="#3b6ef0" d="M6.6 10.8a15 15 0 0 0 6.6 6.6l2.2-2.2c.3-.3.7-.4 1-.2 1.1.4 2.3.6 3.6.6.6 0 1 .4 1 1V20c0 .6-.4 1-1 1A17 17 0 0 1 3 4c0-.6.4-1 1-1h3.5c.6 0 1 .4 1 1 0 1.3.2 2.5.6 3.6.1.3 0 .7-.2 1z"/></svg></span>
    <div><div class="call-label">Call Us</div><div class="call-number">+64 21 0555 0199</div></div>
  </div>
  <a class="btn header-cta" href="#">Get in Touch</a>
</header>

<section class="hero">
  <div class="hero-watermark" aria-hidden="true">Quorvane</div>
  <h1 class="hero-title">Precision.<br>Efficiency.<br>Clarity.</h1>
  <a class="btn hero-cta" href="#">Get in Touch</a>
  <div class="hero-photo" role="img" aria-label="Utility vehicle parked on a grassy alpine hilltop under cloud, framed in a brushed circle"></div>
</section>

<section class="services">
  <h2 class="section-title" style="top:92px">Services offered</h2>
  <article class="service-card" style="left:111px">
    <div class="service-icon"><svg width="34" height="34" viewBox="0 0 24 24" fill="none" stroke="#3b6ef0" stroke-width="1.4"><circle cx="12" cy="12" r="3.5"/><circle cx="12" cy="12" r="7.5" stroke-dasharray="3 2"/></svg></div>
    <h3>Fieldwork Solutions</h3>
    <ul><li>Project management &amp; logistics</li><li>Efficient product rollouts</li><li>Equipment Installation &amp; Maintenance</li></ul>
    <a class="learn" href="#">Learn More</a>
  </article>
  <article class="service-card" style="left:445px">
    <div class="service-icon"><svg width="34" height="34" viewBox="0 0 24 24" fill="none" stroke="#3b6ef0" stroke-width="1.4"><rect x="5" y="4" width="14" height="11"/><path d="M8 12v-2M11 12V8M14 12V6M4 20h16"/></svg></div>
    <h3>Positioning And Monitoring</h3>
    <ul><li>Real-Time Kinematic (RTK) Solutions</li><li>Custom GNSS Base stations</li><li>NTRIP service</li></ul>
    <a class="learn" href="#">Learn More</a>
  </article>
  <article class="service-card" style="left:777px">
    <div class="service-icon"><svg width="34" height="34" viewBox="0 0 24 24" fill="none" stroke="#3b6ef0" stroke-width="1.4"><rect x="4" y="4" width="16" height="16" rx="2"/><circle cx="14" cy="14" r="3"/><path d="M7 7l4 4"/></svg></div>
    <h3>Design And Prototyping</h3>
    <ul><li>Mechanical Component Design</li><li>Robust Field Equipment Infrastructure</li><li>Remote Monitoring System Design</li></ul>
    <a class="learn" href="#">Learn More</a>
  </article>
</section>

<section class="cases">
  <div class="cases-panel">
    <div class="cases-photo" role="img" aria-label="Alpine ridge with a monitoring station overlooking a river valley and distant mountains"></div>
  </div>
  <h2 class="section-title" style="top:110px">Case Studies</h2>
  <article class="case-card featured" style="left:164px;top:211px">
    <div class="case-thumb" role="img" aria-label="Camera mast on rocky alpine terrain"></div>
    <div class="case-body"><h3>Remote camera installation in Alpine Environment.</h3><p>Successful installation of advanced camera systems in the challenging and remote alpine regions of Fiordland.</p><a class="learn" href="#">Learn More</a></div>
  </article>
  <article class="case-card" style="left:627px;top:211px">
    <div class="case-thumb" role="img" aria-label="GNSS station on a mountain summit"></div>
    <div class="case-body"><h3>GNSS CORS station upgrade and survey.</h3><p>Upgrade and reference mark survey of GNSS Continuously Operating Reference Stations (CORS) for the LandBase positioning network.</p><a class="learn" href="#">Learn More</a></div>
  </article>
  <article class="case-card" style="left:164px;top:421px">
    <div class="case-thumb" role="img" aria-label="Satellite equipment frame on a mountain ridge"></div>
    <div class="case-body"><h3>Communications hub upgrade.</h3><p>Installation of a satellite interface for GeoWatch to ensure reliable data transmission for scientific research and monitoring of geological hazards.</p><a class="learn" href="#">Learn More</a></div>
  </article>
  <article class="case-card" style="left:627px;top:421px">
    <div class="case-thumb" role="img" aria-label="Aerial view of damaged railway lines"></div>
    <div class="case-body"><h3>Aerial survey for Post-Disaster Recovery.</h3><p>Survey to assess damage to the railway line caused by Cyclone Gabrielle and create a digital terrain model (DTM) and report.</p><a class="learn" href="#">Learn More</a></div>
  </article>
</section>

<section class="about">
  <h2>About Us</h2>
  <p>Welcome to Quorvane, your reliable partner in delivering innovative solutions. Our team of skilled professionals is committed to excellence, ensuring every project is handled with precision, efficiency, and integrity. We solve problems in the field, build robust infrastructure, and deliver accurate data to our clients. Let us help you achieve your goals with our tailored, sustainable solutions and exceptional service.</p>
  <a class="btn about-cta" href="#">Learn More</a>
  <div class="about-photo" role="img" aria-label="Field equipment on a timber deck and a technician in high-visibility clothing beside a road"></div>
</section>

<section class="contact">
  <h2 class="section-title" style="top:100px">Contact Us</h2>
  <div class="field" style="left:204px;top:191px">Name</div>
  <div class="field" style="left:612px;top:191px">Phone Number</div>
  <div class="field" style="left:204px;top:283px">Email</div>
  <div class="field" style="left:612px;top:283px">How Can We Help You?</div>
  <div class="field message" style="left:204px;top:375px">Message</div>
  <a class="btn submit" href="#">Submit</a>
</section>

<footer class="site-footer">
  <div class="footer-brand"><span class="brand-dot"></span>Quorvane</div>
  <div class="footer-divider"></div>
  <div class="footer-col" style="left:432px"><h4>Quick Links</h4><ul><li>Home</li><li>Services</li><li>Projects</li><li>About</li></ul></div>
  <div class="footer-col" style="left:638px"><h4>Our Company</h4><ul><li>Terms &amp; Conditions</li><li>Privacy Policy</li><li>About Us</li><li>Support</li></ul></div>
  <div class="footer-col" style="left:864px">
    <h4>Contact us</h4>
    <div class="contact-line"><svg width="13" height="16" viewBox="0 0 24 30"><path fill="#fff" d="M12 0a11 11 0 0 0-11 11c0 8 11 19 11 19s11-11 11-19A11 11 0 0 0 12 0zm0 15a4 4 0 1 1 0-8 4 4 0 0 1 0 8z"/></svg><span>Lorem ipsum dolor sit<br>amet, consectetur adipiscing</span></div>
    <div class="contact-line"><svg width="15" height="15" viewBox="0 0 24 24"><path fill="#fff" d="M6.6 10.8a15 15 0 0 0 6.6 6.6l2.2-2.2c.3-.3.7-.4 1-.2 1.1.4 2.3.6 3.6.6.6 0 1 .4 1 1V20c0 .6-.4 1-1 1A17 17 0 0 1 3 4c0-.6.4-1 1-1h3.5c.6 0 1 .4 1 1 0 1.3.2 2.5.6 3.6.1.3 0 .7-.2 1z"/></svg><span>+64 21 0555 0199</span></div>
    <div class="contact-line"><svg width="16" height="12" viewBox="0 0 24 18"><path fill="#fff" d="M0 0h24v18H0z"/><path fill="none" stroke="#2b2b2b" stroke-width="2" d="M1 1l11 9 11-9"/></svg><span>hi@quorvane.nz</span></div>
  </div>
  <div class="footer-bottom"></div>
  <p class="copyright">©Copyrights 2024 Quorvane &nbsp; | &nbsp; All Rights Reserved</p>
</footer>

</body>
</html>
```